Label designs for three different cider varieties

The Larkmoor Perry Works is a family run business. We have been making cider within the family as a hobby for over 100 years and we have recently decided to start to try to sell the cider. Therefore this project is to create a logo and three product labels for three different varieties of cider. So we should end up with four files; one for the logo and one for each of the labels. The files need to be in an editable format for us so that we can add edit the batch numbers e.g. PNG file.
For the logo we would like to use the Pellow Family Shield since Pellow is our family name. We would like it adapted into a cider themed crest, for example with apples and trees. We are open to ideas about the logo but this is just our initial idea. Example of the original Pellow Family Shield can be seen in the link below:
http://www.vinshadeheraldry.net/arms/Pellow-England.jpg
The labels should be no bigger than 93mm in height and 213mm in length. Each label should be similar in style so it is clear the three different varieties of cider are from the same company. Each label must have the following information since this is a legal requirement:
- The logo you have created
- The Larkmoor Perry Works Ltd.
- 52 Mirefield Row, Taunton, Somerset, TA4 9QX
- Alcohol: 6% vol
- 500ml
- Allergens: Contains Sulphites for freshness
- There needs to be space on the label for batch numbers. This is four numbers e.g. 1701.
- Family craft cider makers using only premium apples from our own traditional Somerset orchard.
The names of the three cider varieties are:
- Larkmoor Heritage
- Larkmoor Amber
- Larkmoor Kingsbury
Our initial idea is that each variety would have its own colour associated with it; i.e. black themed label for Larkmoor Heritage, gold themed label for Larkmoor Amber and a red themed label for Larkmoor Kingsbury. The crest logo you have created would then be in the themed colour for that cider variety i.e. black, gold or red.
We would like the labels to reflect the following themes for our brand:
- High end premium brand
- Clean and simple design
- Modern
Overall we are very open to ideas and we do not want to constrain your creativity. All of the above is just our initial ideas but we would love to see what ideas you have. The only things that cannot change are what must be on the label since this is a legal requirement we have to meet.

```html
<!DOCTYPE html>
<html lang="en">
<head>
<meta charset="utf-8">
<title>Larkmoor Perry Works – Cider Labels</title>
<link rel="stylesheet" href="https://fonts.googleapis.com/css2?family=Teko:wght@500;600&family=Saira+Condensed:wght@500;600&display=swap">
<style>
  :root {
    --paper: #ffffff;
    --band: #312823;
    --ink: #2b2522;
    --frame: #6d6d6d;
    --amber: #c9a04a;
    --amber-deep: #7d5f1f;
    --kingsbury: #9e3322;
    --kingsbury-deep: #5a1a10;
    --heritage: #4f8a2a;
    --heritage-deep: #264a12;
    --light: #f4f1ec;
  }
  * { box-sizing: border-box; margin: 0; padding: 0; }
  html, body { width: 872px; height: 1200px; overflow: hidden; background: var(--paper); }
  .sheet { position: relative; width: 872px; height: 1200px; }
  .label {
    position: absolute; left: 0; width: 872px; height: 374px;
    background: var(--paper); border: 1px solid var(--frame); overflow: hidden;
    font-family: "Saira Condensed", "Arial Narrow", sans-serif; color: var(--ink);
  }
  .label--amber { top: 0; --theme: var(--amber); --theme-deep: var(--amber-deep); }
  .label--kingsbury { top: 413px; --theme: var(--kingsbury); --theme-deep: var(--kingsbury-deep); }
  .label--heritage { top: 826px; --theme: var(--heritage); --theme-deep: var(--heritage-deep); }
  .band { position: absolute; left: 0; right: 0; top: 240px; bottom: 0; background: var(--band); }
  .batch { position: absolute; left: 30px; top: 27px; font-size: 12px; font-weight: 600; }
  .address {
    position: absolute; left: 660px; width: 178px; top: 27px; text-align: center;
    font-size: 12px; font-weight: 600; line-height: 16px; font-style: normal;
  }
  .variety {
    position: absolute; left: 0; right: 0; top: 18px; text-align: center;
    font-family: "Teko", "Arial Narrow", sans-serif; font-weight: 600; font-size: 52px;
    line-height: 1; letter-spacing: 1px; color: var(--theme);
    text-shadow: 2px 2px 0 var(--theme-deep);
  }
  .brand-mark {
    position: absolute; left: 337px; width: 200px; top: 76px; height: 160px;
    display: flex; flex-direction: column; align-items: center; gap: 8px;
  }
  .brand-mark__disc { width: 118px; height: 118px; border-radius: 50%; background: var(--theme); }
  .brand-mark__name { font-size: 14px; font-weight: 600; color: var(--theme); white-space: nowrap; }
  .tagline {
    position: absolute; left: 0; right: 0; top: 305px; text-align: center;
    color: var(--light); font-size: 13px; font-weight: 600; line-height: 17px;
  }
  .allergens { position: absolute; left: 27px; top: 330px; color: var(--light); font-size: 9.5px; font-weight: 600; }
  .measures {
    position: absolute; left: 752px; width: 80px; top: 300px; text-align: center;
    color: var(--light); font-family: "Teko", "Arial Narrow", sans-serif; font-weight: 500;
    font-size: 24px; line-height: 23px;
  }
</style>
</head>
<body>
<main class="sheet">

  <section class="label label--amber" aria-label="Larkmoor Amber label">
    <div class="band"></div>
    <p class="batch">Batch Number</p>
    <h1 class="variety">LARKMOOR AMBER</h1>
    <address class="address">The Larkmoor Perry Works Ltd.<br>52 Mirefield Row,<br>Taunton,<br>Somerset,<br>TA4 9QX</address>
    <div class="brand-mark"><span class="brand-mark__disc"></span><span class="brand-mark__name">The Larkmoor Perry Works</span></div>
    <p class="tagline">Family craft cider makers using only premium apples<br>from our own traditional Somerset orchard.</p>
    <p class="allergens">Contains Sulphites For Freshness</p>
    <p class="measures">500ml<br>6% vol</p>
  </section>

  <section class="label label--kingsbury" aria-label="Larkmoor Kingsbury label">
    <div class="band"></div>
    <p class="batch">Batch Number</p>
    <h1 class="variety">LARKMOOR KINGSBURY</h1>
    <address class="address">The Larkmoor Perry Works Ltd.<br>52 Mirefield Row,<br>Taunton,<br>Somerset,<br>TA4 9QX</address>
    <div class="brand-mark"><span class="brand-mark__disc"></span><span class="brand-mark__name">The Larkmoor Perry Works</span></div>
    <p class="tagline">Family craft cider makers using only premium apples<br>from our own traditional Somerset orchard.</p>
    <p class="allergens">Contains Sulphites For Freshness</p>
    <p class="measures">500ml<br>6% vol</p>
  </section>

  <section class="label label--heritage" aria-label="Larkmoor Heritage label">
    <div class="band"></div>
    <p class="batch">Batch Number</p>
    <h1 class="variety">LARKMOOR HERITAGE</h1>
    <address class="address">The Larkmoor Perry Works Ltd.<br>52 Mirefield Row,<br>Taunton,<br>Somerset,<br>TA4 9QX</address>
    <div class="brand-mark"><span class="brand-mark__disc"></span><span class="brand-mark__name">The Larkmoor Perry Works</span></div>
    <p class="tagline">Family craft cider makers using only premium apples<br>from our own traditional Somerset orchard.</p>
    <p class="allergens">Contains Sulphites For Freshness</p>
    <p class="measures">500ml<br>6% vol</p>
  </section>

</main>
</body>
</html>
```